Business Cards, Letterhead, Corporate Materials

Marlowe Building Group, Inc. needs brand identity and marketing materials.

Target Market(s)

Home Owners, Architects, Engineers.

Contact Information for Business Card

Business Cards for myself the President

Font styles to use
Serif

Colors
3377b5
0255a3
cfdfed
cee9f5
86cae7
0393ce
000000
ffffff
f5f5f5

Requirements
Must have
• My name, my address, my email, phone number, company logo, my title. my contractor's license number, web address.
Nice to have
• Very clean professional modern business cards for company president.

```html
<!DOCTYPE html>
<html lang="en">
<head>
<meta charset="utf-8">
<title>Marlowe Building Group — Business Card</title>
<link rel="stylesheet" href="https://fonts.googleapis.com/css2?family=Libre+Baskerville&family=Montserrat:wght@300;600&display=swap">
<style>
  :root {
    --page-bg: #f5f5f5;
    --card-indigo-dark: #272579;
    --card-indigo: #3434a0;
    --band-blue-dark: #0255a3;
    --band-blue: #3377b5;
    --ink-light: #ffffff;
    --ink-soft: #cfdfed;
  }
  html, body {
    margin: 0;
    width: 1200px;
    height: 1022px;
    overflow: hidden;
    background: var(--page-bg);
  }
  .card {
    position: absolute;
    left: 170px;
    top: 261px;
    width: 860px;
    height: 500px;
    border-radius: 6px;
    overflow: hidden;
    background: linear-gradient(135deg, var(--card-indigo) 0%, var(--card-indigo-dark) 100%);
    box-shadow: 0 10px 30px rgba(0, 0, 0, 0.18);
    color: var(--ink-light);
  }
  .card__details {
    position: absolute;
    left: 300px;
    top: 40px;
  }
  .person__name {
    font-family: "Libre Baskerville", serif;
    font-size: 38px;
    margin: 0;
    letter-spacing: 0.5px;
  }
  .person__title {
    font-family: "Libre Baskerville", serif;
    font-size: 17px;
    margin: 6px 0 20px 0;
    color: var(--ink-soft);
  }
  .contact {
    font-family: "Montserrat", sans-serif;
    font-weight: 300;
    font-size: 21px;
    line-height: 30px;
    margin: 0;
  }
  .contact--gap { margin-top: 10px; }
  .brand-band {
    position: absolute;
    left: 0;
    bottom: 0;
    width: 100%;
    height: 140px;
    background: linear-gradient(90deg, var(--band-blue-dark) 0%, var(--band-blue) 100%);
  }
  .brand {
    position: absolute;
    left: 44px;
    top: 44px;
    display: flex;
    align-items: center;
    gap: 18px;
  }
  .brand__mark {
    width: 52px;
    height: 52px;
    background: var(--ink-light);
  }
  .brand__name {
    font-family: "Montserrat", sans-serif;
    font-weight: 600;
    font-size: 30px;
    letter-spacing: 1px;
    color: var(--ink-light);
  }
  .contact-icons {
    position: absolute;
    right: 40px;
    top: 58px;
    display: flex;
    gap: 18px;
  }
  .contact-icons svg { width: 22px; height: 22px; }
</style>
</head>
<body>
  <article class="card">
    <section class="card__details">
      <h1 class="person__name">Daniel Harper</h1>
      <p class="person__title">President</p>
      <p class="contact">48 Foundry Lane</p>
      <p class="contact">Cedar Falls, NY 12480</p>
      <p class="contact contact--gap">+003 5172-4390</p>
      <p class="contact">info@marlowebuilding.com</p>
      <p class="contact">www.marlowebuilding.com</p>
      <p class="contact">Contractor Lic. #MB-204817</p>
    </section>

    <footer class="brand-band">
      <div class="brand">
        <span class="brand__mark" aria-hidden="true"></span>
        <span class="brand__name">MARLOWE BUILDING GROUP, INC.</span>
      </div>
      <div class="contact-icons" aria-hidden="true">
        <svg viewBox="0 0 24 24" fill="none" stroke="#ffffff" stroke-width="2" stroke-linecap="round" stroke-linejoin="round">
          <path d="M5 3h4l2 5-2.5 1.5a11 11 0 0 0 6 6L16 13l5 2v4a2 2 0 0 1-2 2A16 16 0 0 1 3 5a2 2 0 0 1 2-2z"/>
        </svg>
        <svg viewBox="0 0 24 24" fill="none" stroke="#ffffff" stroke-width="2" stroke-linejoin="round">
          <rect x="3" y="5" width="18" height="14" rx="1"/>
          <path d="M3 6l9 7 9-7"/>
        </svg>
        <svg viewBox="0 0 24 24" fill="none" stroke="#ffffff" stroke-width="2">
          <circle cx="12" cy="12" r="9"/>
          <path d="M3 12h18M12 3c3 3 3 15 0 18M12 3c-3 3-3 15 0 18"/>
        </svg>
      </div>
    </footer>
  </article>
</body>
</html>
```